IG ad to attract older men for better health #1

I want a bold headline Instagram Ad that coordinate with my website design with a racy sexy woman to attract men 45yrs old plus. See Two samples attached

Target Market(s)

Men 45 years old and older

Industry/Entity Type

Health And Wellness

Requirements
Must have
• eye catching appeal to men
Nice to have
• The copy to read
Kestrel61go is the headline at the top of the page. Then the copy reads...
"I want to seduce you to better health with a little T&A. Remove the excuses, provide ridiculously simple tips and advice to get you started on a path of lasting heath." Want more?

```html
<!DOCTYPE html>
<html lang="en">
<head>
<meta charset="utf-8">
<title>Kestrel61go – Instagram Ad</title>
<link rel="stylesheet" href="https://fonts.googleapis.com/css2?family=Stardos+Stencil:wght@700&family=Poppins:wght@500;600&display=swap">
<style>
  :root {
    --page: #ffffff;
    --ink-dark: #1b1b1b;
    --panel-dark: #1d1d1d;
    --accent: #f9f530;
    --text-light: #ffffff;
    --skin-light: #a8643c;
    --skin-mid: #6b3a20;
    --skin-deep: #2a1a12;
  }
  * { box-sizing: border-box; margin: 0; padding: 0; }
  html, body { width: 1200px; height: 637px; overflow: hidden; background: var(--page); }
  .canvas { position: relative; width: 1200px; height: 637px; background: var(--page); }

  .ad {
    position: absolute;
    top: 29px;
    width: 520px;
    height: 579px;
    background: var(--panel-dark);
    overflow: hidden;
    font-family: "Poppins", "Century Gothic", sans-serif;
  }
  .ad--yellow-footer { left: 54px; }
  .ad--yellow-band { left: 626px; }

  .ad__photo {
    position: absolute;
    left: 190px;
    top: 0;
    width: 330px;
    height: 515px;
    background:
      radial-gradient(ellipse 38% 30% at 62% 38%, var(--skin-light) 0%, var(--skin-mid) 55%, transparent 100%),
      radial-gradient(ellipse 30% 35% at 55% 80%, var(--skin-mid) 0%, var(--skin-deep) 60%, transparent 100%),
      radial-gradient(ellipse 55% 60% at 65% 50%, var(--skin-deep) 0%, transparent 100%);
  }

  .ad__brand {
    position: absolute;
    left: 21px;
    top: 20px;
    font-family: "Stardos Stencil", "Impact", sans-serif;
    font-weight: 700;
    font-size: 50px;
    line-height: 1;
    color: var(--accent);
    z-index: 2;
  }

  .ad__headline {
    position: absolute;
    left: 21px;
    top: 104px;
    font-weight: 600;
    font-size: 32px;
    line-height: 34px;
    letter-spacing: -0.5px;
    color: var(--text-light);
    z-index: 2;
  }

  .ad__copy {
    position: absolute;
    left: 21px;
    top: 371px;
    font-weight: 600;
    font-size: 20px;
    line-height: 29px;
    letter-spacing: -0.3px;
    color: var(--accent);
    z-index: 2;
  }

  .ad__band {
    position: absolute;
    left: 0;
    top: 367px;
    width: 495px;
    height: 148px;
    background: linear-gradient(90deg, var(--accent) 0%, rgba(249,245,48,0.9) 55%, rgba(249,245,48,0.55) 100%);
    z-index: 1;
  }
  .ad--yellow-band .ad__copy { top: 375px; font-size: 21px; line-height: 31px; color: var(--ink-dark); }

  .ad__footer {
    position: absolute;
    left: 0;
    bottom: 0;
    width: 100%;
    height: 64px;
    display: flex;
    align-items: center;
    padding-left: 21px;
    font-weight: 600;
    font-size: 28px;
    letter-spacing: -0.5px;
    z-index: 2;
  }
  .ad--yellow-footer .ad__footer { background: var(--accent); color: var(--ink-dark); }
  .ad--yellow-band .ad__footer { background: var(--panel-dark); color: var(--text-light); }
</style>
</head>
<body>
<main class="canvas">
  <section class="ad ad--yellow-footer">
    <div class="ad__photo" role="img" aria-label="Photo of a fit, tanned woman in a black sports bra and briefs, posing with hand on hip against a dark background"></div>
    <h1 class="ad__brand">Kestrel61go</h1>
    <p class="ad__headline">I want<br>to seduce<br>you<br>to better<br>health<br>with a little<br>T&amp;A</p>
    <p class="ad__copy">Remove the excuses,<br>provide ridiculously simple tips<br>and advice to get you started<br>on a path of lasting heath</p>
    <p class="ad__footer">Want more?</p>
  </section>

  <section class="ad ad--yellow-band">
    <div class="ad__photo" role="img" aria-label="Photo of a fit, tanned woman in a black sports bra and briefs, posing with hand on hip against a dark background"></div>
    <h1 class="ad__brand">Kestrel61go</h1>
    <p class="ad__headline">I want<br>to seduce<br>you<br>to better<br>health<br>with a little<br>T&amp;A</p>
    <div class="ad__band"></div>
    <p class="ad__copy">Remove the excuses,<br>provide ridiculously simple tips<br>and advice to get you started<br>on a path of lasting heath</p>
    <p class="ad__footer">Want more?</p>
  </section>
</main>
</body>
</html>
```